Linden Medical - Flyer

We are a full service pharmacy that specializes in diabetic testing and medications. We research the patient's insurance to maximize their insurance benefit and then deliver the medications monthly directly to the patient's doorstep, for free! We save the patient, time and money every month.
We would love a flyer that we can distribute to Doctor's offices and patients that sum up our pharmacy. Emphasis on saving money, time, and getting the best quality supplies by maximizing their insurance. We want it to be eye catching, clean, and professional.
You can use our logo or feel free to make your own design.
Updates
Target Market(s)
diabetic patients wanting to save money
Industry/Entity Type
Insurance
Look and feel
Each slider illustrates characteristics of the customer's brand and the style your logo design should communicate.

```html
<!DOCTYPE html>
<html lang="en">
<head>
<meta charset="utf-8">
<title>Linden Medical – Flyer</title>
<link href="https://fonts.googleapis.com/css2?family=Questrial&display=swap" rel="stylesheet">
<style>
  :root {
    --cream: #f4fad6;
    --lime: #b3f542;
    --orange: #e6a03f;
    --white: #ffffff;
    --ink: #2e3328;
    --dot: #b3f542;
  }
  html, body {
    margin: 0;
    padding: 0;
    width: 1200px;
    height: 2400px;
    overflow: hidden;
    background: var(--cream);
  }
  .flyer {
    position: relative;
    width: 1200px;
    height: 2400px;
    overflow: hidden;
    background: var(--cream);
    font-family: "Questrial", "Century Gothic", sans-serif;
    color: var(--ink);
  }
  .flyer__swoosh {
    position: absolute;
    inset: 0;
    width: 1200px;
    height: 2400px;
  }
  .swoosh-orange { fill: var(--orange); }
  .swoosh-white { fill: var(--white); }
  .swoosh-lime { fill: var(--lime); }

  .brand {
    position: absolute;
    top: 120px;
    right: 40px;
    display: flex;
    align-items: center;
    gap: 24px;
  }
  .brand__dot {
    width: 84px;
    height: 84px;
    border-radius: 50%;
    background: var(--lime);
  }
  .brand__name {
    font-size: 74px;
    line-height: 1;
    color: var(--ink);
    letter-spacing: 1px;
    white-space: nowrap;
  }

  .headline {
    position: absolute;
    top: 640px;
    left: 246px;
    width: 800px;
    margin: 0;
    text-align: center;
    font-size: 66px;
    font-weight: 400;
    line-height: 68px;
  }

  .benefits {
    position: absolute;
    top: 818px;
    left: 223px;
    width: 900px;
    margin: 0;
    padding: 0;
    list-style: none;
  }
  .benefits li {
    display: flex;
    align-items: center;
    height: 48px;
    margin-bottom: 61px;
    font-size: 42px;
    line-height: 48px;
    white-space: nowrap;
  }
  .benefits li::before {
    content: "";
    flex: 0 0 48px;
    height: 48px;
    margin-right: 32px;
    border-radius: 50%;
    background: var(--dot);
  }

  .contact {
    position: absolute;
    top: 2005px;
    left: 0;
    width: 1200px;
    margin: 0;
    text-align: center;
    font-size: 52px;
    line-height: 1;
    font-style: normal;
  }
  .contact span {
    display: block;
    height: 89px;
    white-space: nowrap;
  }
</style>
</head>
<body>
  <main class="flyer">
    <svg class="flyer__swoosh" viewBox="0 0 650 1300" preserveAspectRatio="none" aria-hidden="true">
      <path class="swoosh-white" d="M0 0 H252 C160 65 55 180 0 328 Z"/>
      <path class="swoosh-orange" d="M0 0 H246 C152 63 50 176 0 320 Z"/>
      <path class="swoosh-lime" d="M0 0 H226 C138 58 45 160 0 292 Z"/>
      <path class="swoosh-orange" d="M0 810 C70 940 200 998 340 995 C450 992 560 942 650 898 V1300 H0 Z"/>
      <path class="swoosh-white" d="M0 940 C80 1012 200 1046 330 1046 C450 1046 560 962 650 900 V1300 H0 Z"/>
      <path class="swoosh-lime" d="M0 950 C80 1020 200 1053 330 1053 C452 1053 565 966 650 905 V1300 H0 Z"/>
    </svg>

    <header class="brand">
      <span class="brand__dot"></span>
      <span class="brand__name">Linden Medical</span>
    </header>

    <h1 class="headline">Your diabetic pharmacy,<br>delivered free</h1>

    <ul class="benefits">
      <li>Diabetic testing supplies &amp; medications</li>
      <li>We research your insurance for you</li>
      <li>Maximize every insurance benefit</li>
      <li>Top-quality supplies at the lowest cost</li>
      <li>Free monthly delivery to your door</li>
      <li>Save time and money every month</li>
      <li>Full service pharmacy care</li>
    </ul>

    <address class="contact">
      <span>Telephone: (555) 014-2273</span>
      <span>Email: care@lindenmedical-rx.com</span>
      <span>Website: www.lindenmedical-rx.com</span>
      <span>Address: 48 Birchwood Ave, Fairview</span>
    </address>
  </main>
</body>
</html>
```